Web design project for exciting Australian start-up

Background
We are looking for a creative and talented web design artist to work alongside our market leading web developer.
• You will be required to create a modern and clean design theme for our website, incorporating selected rustic colour scheme elements for our exciting Australian start-up to operate within the coffee industry.
reoccurring work to be expected to flow to the successful designer.
Requirements
• c. 5 - 10 page website
• Landing page
• Log in/ out
• 404 template
• Typography is emphasised
• Please use either a) quillnest.com, b) free web fonts, c) plovra fonts
• All design elements in vector format
• Preferably with icons for each header title(i.e. about us, how it works etc) but designer have free reign over how the site looks, so might not be applicable
• All pages to be responsive
• Down to Kelvo resolution

High level visual design brief attached - additional pages to be worked from base design.

Design inspiration
• We would like to use design elements from the following sources:
http://www.plovra.com/vintel/ (Functionality)
Colour scheme refer to logo and complementary style guide

```html
<!DOCTYPE html>
<html lang="en">
<head>
<meta charset="utf-8">
<title>Brewhaven – Dashboard</title>
<link href="https://fonts.googleapis.com/css2?family=Open+Sans:wght@300;400;600;700;800&display=swap" rel="stylesheet">
<style>
:root{
  --orange:#ff6a00;
  --orange-bar:#ff8a00;
  --ink:#1a1a1a;
  --grey-text:#444;
  --panel:#f4f4f4;
  --panel-line:#e3e3e3;
  --dark-btn:#3a3a3a;
  --footer:#000;
  --white:#fff;
}
*{margin:0;padding:0;box-sizing:border-box}
html,body{width:1200px;height:997px;overflow:hidden}
body{font-family:"Open Sans",Arial,sans-serif;color:var(--ink);background:var(--white);position:relative}
a{color:inherit;text-decoration:none}

.site-header{position:absolute;left:0;top:0;width:1200px;height:108px}
.brand{position:absolute;left:157px;top:30px;font-weight:800;font-size:30px;letter-spacing:1px;color:var(--ink);display:flex;align-items:center;gap:10px}
.brand-mark{width:40px;height:40px;border-radius:50%;background:var(--orange-bar)}
.auth{position:absolute;left:868px;top:33px;display:flex;height:36px}
.auth a{display:flex;align-items:center;justify-content:center;color:var(--white);font-weight:700;font-size:14px}
.btn-login{background:var(--orange);width:83px}
.btn-signup{background:var(--dark-btn);width:83px}
.header-rule{position:absolute;left:0;top:108px;width:1200px;height:8px;background:var(--orange-bar)}

.panel{position:absolute;background:var(--panel);border:1px solid var(--panel-line)}
.panel-title{font-weight:600;font-size:13.5px;color:#333}

.profile{left:165px;top:126px;width:206px;height:247px;padding:17px 16px}
.profile-photo{margin-top:6px;width:172px;height:129px;background:linear-gradient(135deg,#7a4a24,#3b2010 55%,#a57a52)}
.profile-name{margin-top:7px;font-size:16px;font-weight:300;color:var(--orange)}
.profile-meta{font-size:13.5px;font-weight:600;line-height:20px}

.account{left:165px;top:388px;width:206px;height:244px;padding:12px 16px}
.account-item{position:relative;padding-left:12px;margin-top:18px}
.account-item .icon{position:absolute;left:-14px;top:2px}
.account-item h3{font-size:13.5px;font-weight:600;color:#333}
.account-item p{font-size:13.5px;font-weight:300;color:var(--grey-text);line-height:20px;margin-top:1px}

.section-bar{position:absolute;left:387px;width:427px;height:49px;background:var(--panel);border:1px solid var(--panel-line);padding:15px 14px;font-weight:600;font-size:13.5px;color:var(--orange)}
.timer{position:absolute;left:390px;top:197px}
.timer-label{display:flex;align-items:center;gap:9px;font-size:13.5px;color:#333}
.timer-value{font-weight:700;font-size:29px;color:var(--orange);letter-spacing:1px;margin:4px 0 0 3px}
.filters{position:absolute;left:401px;top:355px;display:flex;font-weight:600;font-size:14px;color:var(--orange)}
.filters span{display:flex;align-items:center;gap:6px}
.filters span::before{content:"";border-left:5px solid #555;border-top:3.5px solid transparent;border-bottom:3.5px solid transparent}

.side{left:831px;top:126px;width:205px;height:329px;padding:8px 10px}
.inbox{display:flex;align-items:center;gap:10px;height:35px;background:var(--orange);color:var(--white);font-weight:700;font-size:14px;padding-left:7px}
.side-link{display:flex;align-items:center;gap:7px;font-size:11.5px;color:#333;margin-left:6px}
.side-link::before{content:"";width:5px;height:5px;border-right:1.6px solid var(--orange);border-top:1.6px solid var(--orange);transform:rotate(45deg)}
.deliveries{position:absolute;left:13px;top:166px;width:162px;height:148px;background:var(--white);border:1px solid #ddd;border-radius:3px;padding:8px 7px;overflow:hidden}
.delivery{margin-bottom:14px}
.delivery .time{font-size:12.5px;font-weight:300;color:#333}
.delivery .title{font-size:13px;font-weight:600}
.delivery .order{font-size:11px;font-weight:300;color:#333}
.scroll-track{position:absolute;left:182px;top:166px;width:14px;height:148px;background:var(--white);border:1px solid #ddd;border-radius:4px}
.scroll-thumb{position:absolute;left:3px;top:3px;width:6px;height:38px;background:var(--orange);border-radius:3px}

.calendar{position:absolute;left:831px;top:468px;width:205px}
.cal-head{height:30px;background:var(--orange);color:var(--white);font-size:11.5px;display:flex;align-items:center;justify-content:space-between;padding:0 8px}
.cal-grid{display:grid;grid-template-columns:repeat(7,1fr);border-left:1px solid var(--panel-line)}
.cal-dow{font-size:7px;font-weight:600;text-align:center;padding:7px 0 4px;color:#333}
.cal-day{height:29px;border-right:1px solid var(--panel-line);border-bottom:1px solid var(--panel-line);font-size:8.5px;font-weight:600;display:flex;align-items:center;justify-content:center;position:relative}
.cal-day.muted{color:#999;font-weight:400}
.cal-day.event::after{content:"";position:absolute;bottom:5px;width:2px;height:2px;background:#333;border-radius:50%}
.cal-day.today{background:var(--orange-bar);color:var(--white)}
.cal-day.today::after{background:var(--white)}
.download{position:absolute;left:853px;top:678px;display:flex;align-items:center;gap:10px;font-weight:700;font-size:16px;color:#555}
.download-icon{width:38px;height:40px;background:linear-gradient(#5fbf3a,#2f8d1f);border-radius:2px}

.site-footer{position:absolute;left:0;top:737px;width:1200px;height:260px;background:var(--footer);color:var(--white)}
.footer-col{position:absolute;top:45px}
.footer-col h4{font-size:13.5px;font-weight:700;margin-bottom:18px}
.footer-col li{list-style:none;font-size:13.5px;font-weight:300;line-height:20.5px}
.social li{display:flex;justify-content:space-between;width:129px;line-height:22px}
.social i{width:19px;height:19px;border-radius:50%;margin-top:2px}
.copyright{position:absolute;left:0;width:1200px;top:195px;text-align:center;font-size:13.5px;font-weight:300}
</style>
</head>
<body>
<header class="site-header">
  <div class="brand"><span class="brand-mark"></span>BREWHAVEN</div>
  <nav class="auth"><a class="btn-login" href="#">LOGIN</a><a class="btn-signup" href="#">SIGN UP</a></nav>
</header>
<div class="header-rule"></div>

<aside class="panel profile">
  <div class="panel-title">Photos</div>
  <div class="profile-photo" role="img" aria-label="Sack of roasted coffee beans with a cup of coffee"></div>
  <div class="profile-name">Café Morrow</div>
  <div class="profile-meta">Melbourne, Australia<br>Member since [Feb, 2014]</div>
</aside>

<section class="panel account">
  <div class="panel-title">My Account</div>
  <div class="account-item">
    <svg class="icon" width="26" height="18" viewBox="0 0 26 18"><rect x="0.5" y="0.5" width="25" height="17" fill="var(--orange)"/><path d="M1 1l12 9 12-9M1 17l9-8M25 17l-9-8" stroke="#fff" stroke-width="1.3" fill="none"/></svg>
    <h3>Email Address</h3><p>Verified</p>
  </div>
  <div class="account-item">
    <svg class="icon" width="26" height="22" viewBox="0 0 26 22"><path d="M2 8h18v4a8 8 0 0 1-8 8h-2a8 8 0 0 1-8-8z" fill="var(--orange)"/><path d="M20 10h3a2 2 0 0 1 0 4h-4" stroke="var(--orange)" stroke-width="2" fill="none"/><path d="M8 1v4M11 1v4M14 1v4" stroke="var(--orange)" stroke-width="1.4"/></svg>
    <h3>Café type</h3><p>(i.e. Café, speciality coffee shop, restaurant)</p>
  </div>
  <div class="account-item">
    <svg class="icon" width="28" height="20" viewBox="0 0 28 20"><rect x="10" y="1" width="17" height="3" fill="var(--orange)"/><rect x="10" y="6" width="17" height="3" fill="var(--orange)"/><rect x="10" y="11" width="17" height="3" fill="var(--orange)"/><circle cx="8" cy="13" r="7" fill="var(--orange)"/><text x="8" y="17" font-size="10" font-weight="700" fill="#fff" text-anchor="middle" font-family="Open Sans, sans-serif">$</text></svg>
    <h3>Payment details</h3><p>Verified</p>
  </div>
</section>

<main>
  <div class="section-bar" style="top:126px">Live tenders</div>
  <div class="timer">
    <div class="timer-label"><svg width="21" height="21" viewBox="0 0 21 21"><circle cx="10.5" cy="10.5" r="9.3" fill="none" stroke="#333" stroke-width="1.8"/><path d="M10.5 5v6h4" stroke="#333" stroke-width="1.8" fill="none"/></svg>Time Remaning</div>
    <div class="timer-value">44 : 22 : 27</div>
  </div>
  <div class="section-bar" style="top:289px">Purchases</div>
  <div class="filters">
    <span style="width:110px">All</span>
    <span style="width:148px">Period (x months)</span>
    <span>Awaiting feedback (x)</span>
  </div>
</main>

<aside class="panel side">
  <div class="inbox"><svg width="26" height="18" viewBox="0 0 26 18"><rect x="0.5" y="0.5" width="25" height="17" fill="none" stroke="#fff"/><path d="M1 1l12 9 12-9M1 17l9-8M25 17l-9-8" stroke="#fff" stroke-width="1.2" fill="none"/></svg>Inbox</div>
  <div class="side-link" style="margin-top:16px">Messages</div>
  <div class="side-link" style="margin-top:22px">Saved Searches</div>
  <div class="side-link" style="margin-top:28px">Incoming Deliveries This Week</div>
  <div class="deliveries">
    <div class="delivery"><div class="time">8 am – 11 am</div><div class="title">Delivery of order 3220x</div><div class="order">Order: 20kg Hillcrest Beans</div></div>
    <div class="delivery"><div class="time">8 am – 11 am</div><div class="title">Delivery of order 3220x</div><div class="order">Order: 20kg Hillcrest Beans</div></div>
  </div>
  <div class="scroll-track"><div class="scroll-thumb"></div></div>
</aside>

<section class="calendar">
  <div class="cal-head">
    <svg width="8" height="10" viewBox="0 0 8 10"><path d="M6 1L2 5l4 4" stroke="#fff" stroke-width="2" fill="none"/></svg>
    <span>February 2014</span>
    <svg width="8" height="10" viewBox="0 0 8 10"><path d="M2 1l4 4-4 4" stroke="#fff" stroke-width="2" fill="none"/></svg>
  </div>
  <div class="cal-grid" style="border-left:none">
    <div class="cal-dow">MON</div><div class="cal-dow">TUE</div><div class="cal-dow">WED</div><div class="cal-dow">THU</div><div class="cal-dow">FRI</div><div class="cal-dow">SAT</div><div class="cal-dow">SUN</div>
  </div>
  <div class="cal-grid" style="border-top:1px solid var(--panel-line)">
    <div class="cal-day muted event">30</div><div class="cal-day">1</div><div class="cal-day event">2</div><div class="cal-day">3</div><div class="cal-day">4</div><div class="cal-day">5</div><div class="cal-day">6</div>
    <div class="cal-day">7</div><div class="cal-day">8</div><div class="cal-day">9</div><div class="cal-day">10</div><div class="cal-day">11</div><div class="cal-day today event">12</div><div class="cal-day">13</div>
    <div class="cal-day">14</div><div class="cal-day">15</div><div class="cal-day event">16</div><div class="cal-day event">17</div><div class="cal-day">18</div><div class="cal-day">19</div><div class="cal-day">20</div>
    <div class="cal-day event">21</div><div class="cal-day">22</div><div class="cal-day">23</div><div class="cal-day">24</div><div class="cal-day">25</div><div class="cal-day">26</div><div class="cal-day">27</div>
    <div class="cal-day">28</div><div class="cal-day">29</div><div class="cal-day">30</div><div class="cal-day">31</div><div class="cal-day muted">1</div><div class="cal-day muted">2</div><div class="cal-day muted">3</div>
  </div>
</section>

<a class="download" href="#"><span class="download-icon"></span>Download Now</a>

<footer class="site-footer">
  <div class="footer-col" style="left:166px">
    <h4>Helpful info</h4>
    <ul><li>About us</li><li>Media enquiries</li><li>Terms &amp; conditions</li><li>Privacy policy</li></ul>
  </div>
  <div class="footer-col" style="left:538px">
    <h4>Who we are Join us on</h4>
    <ul><li>How it works</li><li>FAQ</li><li>Contact us</li></ul>
  </div>
  <div class="footer-col social" style="left:906px">
    <h4>Join us on</h4>
    <ul>
      <li>Friendlane<i style="background:#3b5998"></i></li>
      <li>Chirpline<i style="background:#33ccff"></i></li>
      <li>Workweave<i style="background:#0077b5"></i></li>
      <li>Vidstream<i style="background:#e52d27"></i></li>
    </ul>
  </div>
  <div class="copyright">Copyright © 2014 Brewhaven</div>
</footer>
</body>
</html>
```